Harbor Ridge Chapel
Every Man, Woman, and Child
Modern
Mark Fenwick
lead Pastor
4527 Delford
Lindenport, CA 90417
mark.fenwick@harborridgechapel.example
harborridgechapel.example
front of the card is the logo, and all the info on the back
use the logo, and try harbor ridge chapel behind the logo and try it under the logo.

```html
<!DOCTYPE html>
<html lang="en">
<head>
<meta charset="utf-8">
<title>Harbor Ridge Chapel – Stationery Set</title>
<link href="https://fonts.googleapis.com/css2?family=Montserrat:wght@400;600;700&family=Open+Sans:wght@400;600&display=swap" rel="stylesheet">
<style>
  :root{
    --bg-dark:#2b2c2e;
    --bg-mid:#4a4b4e;
    --ink:#111213;
    --paper:#ffffff;
    --paper-shade:#eef0f2;
    --brand-blue:#1f7fc4;
    --brand-blue-dark:#15609a;
    --mist:#e6ebf1;
    --label:#c9cbcf;
    --muted:#8a8d92;
    --white:#ffffff;
  }
  *{box-sizing:border-box;margin:0;padding:0}
  html,body{width:1200px;height:427px;overflow:hidden}
  body{
    position:relative;
    background:linear-gradient(160deg,var(--bg-mid) 0%,var(--bg-dark) 60%,#202123 100%);
    font-family:"Open Sans",Arial,sans-serif;
    color:var(--white);
  }

  /* brand block */
  .brand{position:absolute;left:8px;top:14px;width:128px;text-align:center}
  .brand-mark{width:40px;height:40px;border-radius:50%;background:var(--brand-blue);margin:0 auto 8px}
  .brand-name{font-family:"Montserrat",Arial,sans-serif;font-weight:700;font-size:13px;line-height:1.15;text-transform:uppercase}
  .brand-tagline{font-size:6.5px;color:var(--brand-blue);margin-top:5px}

  .item-label{position:absolute;font-size:6px;color:var(--label);text-align:center}

  /* business card */
  .business-card{position:absolute;left:12px;top:175px;width:122px;height:77px;background:var(--ink);border-radius:3px;overflow:hidden;box-shadow:0 3px 8px rgba(0,0,0,.5)}
  .business-card svg{position:absolute;left:0;bottom:0}
  .card-name{position:absolute;left:9px;top:9px;font-family:"Montserrat",Arial,sans-serif;font-weight:600;font-size:7px}
  .card-role{position:absolute;left:9px;top:18px;font-size:4.6px;color:var(--label)}
  .card-contact{position:absolute;left:9px;top:28px;font-size:4px;line-height:1.5;color:var(--label)}

  /* letterhead */
  .letterhead{position:absolute;top:24px;width:259px;height:379px;background:var(--paper);box-shadow:0 4px 10px rgba(0,0,0,.55);overflow:hidden}
  .letterhead .header{position:absolute;left:0;top:0}
  .lh-brand{position:absolute;left:92px;top:14px;display:flex;align-items:center;gap:4px}
  .lh-brand .dot{width:14px;height:14px;border-radius:50%;background:var(--brand-blue)}
  .lh-brand span{font-family:"Montserrat",Arial,sans-serif;font-weight:700;font-size:5.5px;text-transform:uppercase;line-height:1.1;width:58px}
  .lh-contact{position:absolute;left:170px;top:10px;padding-left:5px;border-left:1px solid #555;font-size:3.8px;line-height:1.55;color:var(--label)}
  .watermark{position:absolute;left:22px;top:72px;width:200px;height:200px;border-radius:50%;background:var(--mist);opacity:.7}
  .lh-footer{position:absolute;left:0;right:0;bottom:8px;text-align:center;font-size:3.8px;color:var(--muted)}

  /* envelopes */
  .envelope{position:absolute;background:var(--paper);box-shadow:0 3px 8px rgba(0,0,0,.5);overflow:hidden}
  .env-brand{display:flex;align-items:center;gap:4px;font-size:4.5px;color:var(--white)}
  .env-brand .dot{width:10px;height:10px;border-radius:50%;background:var(--brand-blue)}

  .env-front{left:828px;top:24px;width:336px;height:72px}
  .env-front .band{position:absolute;left:0;top:0;width:100%;height:18px;background:var(--ink)}
  .env-front .env-brand{position:absolute;left:140px;top:4px}

  .env-back{left:828px;top:101px;width:336px;height:72px}
  .env-back svg{position:absolute;left:0;top:0}
  .env-back .env-brand{position:absolute;left:122px;top:7px}

  .env-open{left:828px;top:180px;width:336px;height:67px}
  .env-open svg{position:absolute;left:0;top:0}

  .env-small{left:816px;top:259px;width:276px;height:132px}
  .env-small svg.band{position:absolute;left:0;top:0}
  .env-small .env-brand{position:absolute;left:10px;top:10px;font-family:"Montserrat",Arial,sans-serif;font-weight:700;font-size:5px;text-transform:uppercase}
  .env-small .mini-watermark{position:absolute;right:18px;bottom:10px;width:62px;height:62px;border-radius:50%;background:var(--mist);opacity:.8}
</style>
</head>
<body>

  <header class="brand">
    <div class="brand-mark"></div>
    <div class="brand-name">Harbor Ridge<br>Chapel</div>
    <div class="brand-tagline">Every Man, Woman, and Child</div>
  </header>

  <div class="business-card">
    <div class="card-name">Mark Fenwick</div>
    <div class="card-role">Lead Pastor</div>
    <div class="card-contact">4527 Delford<br>Lindenport, CA 90417<br>mark.fenwick@harborridgechapel.example<br>harborridgechapel.example</div>
    <svg width="122" height="24" viewBox="0 0 122 24">
      <path d="M0 12 C40 2 80 22 122 6 L122 24 L0 24Z" fill="var(--brand-blue)"/>
      <path d="M0 18 C40 10 80 26 122 14 L122 24 L0 24Z" fill="var(--white)"/>
    </svg>
  </div>
  <div class="item-label" style="left:12px;top:284px;width:122px">Business Card</div>

  <article class="letterhead" style="left:240px">
    <svg class="header" width="259" height="58" viewBox="0 0 259 58">
      <path d="M0 0 H259 V42 C190 54 90 32 0 50Z" fill="var(--ink)"/>
      <path d="M0 50 C90 32 190 54 259 42" stroke="var(--brand-blue)" stroke-width="2" fill="none"/>
    </svg>
    <div class="lh-brand"><div class="dot"></div><span>Harbor Ridge Chapel</span></div>
    <div class="lh-contact">4527 Delford<br>Lindenport, CA 90417<br>harborridgechapel.example</div>
    <div class="watermark"></div>
  </article>
  <div class="item-label" style="left:240px;top:408px;width:259px">Letterhead Version A</div>

  <article class="letterhead" style="left:509px">
    <svg class="header" width="259" height="58" viewBox="0 0 259 58">
      <path d="M0 0 H259 V42 C190 54 90 32 0 50Z" fill="var(--ink)"/>
      <path d="M0 50 C90 32 190 54 259 42" stroke="var(--brand-blue)" stroke-width="2" fill="none"/>
    </svg>
    <div class="lh-brand"><div class="dot"></div><span>Harbor Ridge Chapel</span></div>
    <div class="lh-contact">4527 Delford<br>Lindenport, CA 90417<br>harborridgechapel.example</div>
    <div class="watermark"></div>
    <div class="lh-footer">4527 Delford · Lindenport, CA 90417 · harborridgechapel.example</div>
  </article>
  <div class="item-label" style="left:509px;top:408px;width:259px">Letterhead Version B</div>

  <div class="envelope env-front">
    <div class="band"></div>
    <div class="env-brand"><div class="dot"></div>harborridgechapel.example</div>
  </div>

  <div class="envelope env-back">
    <svg width="336" height="72" viewBox="0 0 336 72">
      <path d="M0 0 H336 V8 L168 46 L0 8Z" fill="var(--brand-blue)"/>
      <path d="M0 8 L168 46 L336 8" stroke="var(--brand-blue-dark)" stroke-width="1.2" fill="none"/>
    </svg>
    <div class="env-brand"><div class="dot"></div>harborridgechapel.example</div>
  </div>

  <div class="envelope env-open">
    <svg width="336" height="67" viewBox="0 0 336 67">
      <path d="M0 0 L168 36 L336 0Z" stroke="#cfd3d8" stroke-width="1" fill="var(--paper-shade)"/>
      <path d="M0 67 L140 30 M336 67 L196 30" stroke="#dde0e4" stroke-width="1" fill="none"/>
    </svg>
  </div>

  <div class="envelope env-small">
    <svg class="band" width="276" height="34" viewBox="0 0 276 34">
      <path d="M0 0 H276 V24 C190 32 90 20 0 30Z" fill="var(--ink)"/>
      <path d="M0 30 C90 20 190 32 276 24" stroke="var(--brand-blue)" stroke-width="2" fill="none"/>
    </svg>
    <div class="env-brand"><div class="dot"></div>Harbor Ridge Chapel</div>
    <div class="mini-watermark"></div>
  </div>
  <div class="item-label" style="left:828px;top:408px;width:336px">Envelope Front and Back</div>

</body>
</html>
```